Harvest Moon's Riddle Event Flyer - Fundraiser for a High Council Candidate

Working on an event flyer for a fundraiser for a Verdantist candidate for Council in Tennessee. Hosting an event for him that's a Harvest Moon's Riddle theme, and I need a cool flyer that fits the theme with event details.
Host names will be added to the flyer on an ongoing basis, so will need someone who can quickly add names to flyer as hosts commit. Would like to agree to a fee for all work up front.
I'm attaching a mockup of a flyer that my friend did, before he had to back out because of work commitments, as well as a couple of pieces of Harvest Moon's Riddle art that I think are cool.
Verdantist

```html
<!DOCTYPE html>
<html lang="en">
<head>
<meta charset="utf-8">
<title>Harvest Moon's Riddle – Reception Flyer</title>
<link rel="stylesheet" href="https://fonts.googleapis.com/css2?family=Cinzel:wght@500;600&family=Open+Sans:wght@300;400&display=swap">
<style>
  :root {
    --night-deep: #151c5a;
    --night: #1f2a74;
    --night-glow: #283a8a;
    --ink-white: #ffffff;
    --card-white: #fbfbfb;
    --ember: #de5a1f;
    --ring: #c9c6e6;
    --bloom-pale: #a9dcf4;
    --bloom-light: #6cc0ec;
    --bloom: #3f9fd6;
    --bloom-dark: #1e6fae;
  }
  * { margin: 0; padding: 0; box-sizing: border-box; }
  html, body { width: 928px; height: 1200px; overflow: hidden; }
  body { background: var(--night-deep); }
  .flyer {
    position: relative;
    width: 928px; height: 1200px;
    overflow: hidden;
    background: radial-gradient(ellipse at 50% 45%, var(--night-glow) 0%, var(--night) 45%, var(--night-deep) 100%);
    font-family: "Open Sans", Arial, sans-serif;
    color: var(--ink-white);
  }
  .starfield { position: absolute; inset: 0; }
  .invite-line {
    position: absolute; top: 52px; left: 0; width: 100%;
    text-align: center; font-weight: 300; font-size: 30px;
  }
  .invite-line .diamond {
    display: inline-block; width: 9px; height: 9px; background: var(--ember);
    transform: rotate(45deg); vertical-align: middle; margin: 0 10px 4px;
  }
  .emblem { position: absolute; left: 0; top: 0; }
  .event-title { font-weight: 600; }
  .title {
    position: absolute; left: 232px; width: 500px; text-align: center;
    font-family: "Cinzel", Georgia, serif; font-weight: 600; color: var(--ember);
    line-height: 1; white-space: nowrap;
  }
  .title-article { top: 328px; font-size: 46px; }
  .title-main { top: 400px; font-size: 52px; }
  .title-sub { top: 490px; font-size: 42px; }
  .details {
    position: absolute; left: 0; width: 100%; text-align: center;
    font-weight: 300; font-size: 31px; line-height: 43px;
  }
  .details-reception { top: 853px; }
  .details-venue { top: 975px; }
  .candidate { color: var(--ember); font-weight: 400; }
  .paid-for {
    position: absolute; top: 1103px; left: 0; width: 100%; text-align: center;
    font-size: 22px; font-weight: 400; color: var(--ember);
  }
</style>
</head>
<body>
<main class="flyer">
  <svg class="starfield" width="928" height="1200" viewBox="0 0 928 1200" role="img" aria-label="Night sky scattered with small stars">
    <rect width="928" height="1200" fill="none"/>
  </svg>

  <p class="invite-line"><span class="diamond"></span>You are cordially invited to<span class="diamond"></span></p>

  <svg class="emblem" width="928" height="1200" viewBox="0 0 928 1200">
    <defs>
      <radialGradient id="wreath-tone" cx="480" cy="470" r="345" gradientUnits="userSpaceOnUse">
        <stop offset="0.78" stop-color="var(--bloom-pale)"/>
        <stop offset="0.86" stop-color="var(--bloom-light)"/>
        <stop offset="0.93" stop-color="var(--bloom)"/>
        <stop offset="1" stop-color="var(--bloom-dark)" stop-opacity="0"/>
      </radialGradient>
    </defs>
    <path class="floral-wreath" role="img" aria-label="Watercolour wreath of blue flowers and leaves around the title"
      fill="url(#wreath-tone)" fill-rule="evenodd" opacity="0.9"
      d="M480 125a345 345 0 1 0 0.1 0z M480 190a280 280 0 1 1 -0.1 0z"/>
    <circle class="frame-ring" cx="480" cy="470" r="296" fill="none" stroke="var(--ring)" stroke-width="8" opacity="0.75"/>
    <circle class="title-disc" cx="480" cy="470" r="280" fill="var(--card-white)"/>
    <g class="flourish" role="img" aria-label="Orange scroll flourish">
      <rect x="384" y="351" width="70" height="4" rx="2" fill="var(--ember)"/>
      <rect x="506" y="351" width="70" height="4" rx="2" fill="var(--ember)"/>
    </g>
    <g class="rule" fill="var(--ember)" stroke="var(--ember)">
      <line x1="246" y1="467" x2="720" y2="467" stroke-width="2"/>
      <rect x="242" y="463" width="7" height="7" transform="rotate(45 245.5 466.5)"/>
      <rect x="480" y="463" width="7" height="7" transform="rotate(45 483.5 466.5)"/>
      <rect x="716" y="463" width="7" height="7" transform="rotate(45 719.5 466.5)"/>
      <line x1="246" y1="552" x2="720" y2="552" stroke-width="2"/>
      <rect x="242" y="548" width="7" height="7" transform="rotate(45 245.5 551.5)"/>
      <rect x="480" y="548" width="7" height="7" transform="rotate(45 483.5 551.5)"/>
      <rect x="716" y="548" width="7" height="7" transform="rotate(45 719.5 551.5)"/>
    </g>
    <g class="flourish" role="img" aria-label="Orange scroll flourish">
      <rect x="362" y="598" width="236" height="4" rx="2" fill="var(--ember)"/>
    </g>
  </svg>

  <h1 class="event-title">
    <span class="title title-article">A</span>
    <span class="title title-main">Harvest Moon’s</span>
    <span class="title title-sub">Vnc Meeting Riddle</span>
  </h1>

  <p class="details details-reception">Reception for <span class="candidate">Tobias Wrenfield</span><br>Wednesday August 23rd 6–9 p.m.</p>
  <p class="details details-venue">House of Calvin Ashmore<br>418B, Larkspur Ave, Nashville TN 37216</p>

  <p class="paid-for">Paid for Wrenfield for High Council</p>
</main>
</body>
</html>
```